Tembo & Lusani Advocates website

An interactive professional law firm website fully synchronized with social media pages.

Target Market(s)

Corporations and professionals

Industry/Entity Type

Professional Service

Number of Pages Required

5+ page

Font styles to use
Sans Serif

Colors

Designer to choose colors to be used in the design.

```html
<!DOCTYPE html>
<html lang="en">
<head>
<meta charset="utf-8">
<title>Tembo &amp; Lusani Advocates</title>
<link href="https://fonts.googleapis.com/css2?family=Roboto:wght@400;500;700&display=swap" rel="stylesheet">
<style>
:root{
  --brand:#8c1119;
  --brand-dark:#6f0c13;
  --ink:#333;
  --muted:#666;
  --line:#e4e4e4;
  --tile:#f7f7f7;
  --white:#fff;
}
*{margin:0;padding:0;box-sizing:border-box}
html,body{width:1200px;height:1200px;overflow:hidden;background:var(--white)}
body{font-family:'Roboto',sans-serif;color:var(--ink);position:relative;letter-spacing:.04em}
.hero{position:absolute;left:171px;top:0;width:836px;height:316px;
  background:linear-gradient(160deg,#4c5660 0%,#1f2c3d 35%,#3d4c63 55%,#233149 75%,#4a5970 100%)}
.nav{position:absolute;left:73px;top:0;width:692px;height:59px;background:rgba(255,255,255,.94);display:flex;align-items:center}
.brand{display:flex;align-items:center;gap:8px;margin-left:14px;font-size:13px;font-weight:500;color:var(--brand);letter-spacing:.02em}
.brand-mark{width:12px;height:12px;background:var(--brand)}
.menu{position:absolute;left:318px;top:0;display:flex;height:59px;font-size:11px;color:var(--ink)}
.menu a{display:flex;align-items:center;padding:0 7px;text-decoration:none;color:inherit}
.menu a.active{background:var(--brand);color:var(--white);font-weight:700;padding:0 10px;margin-right:4px}
.hero-copy{position:absolute;top:175px;width:100%;text-align:center;color:var(--white)}
.hero-copy p{font-size:12.5px;letter-spacing:.06em}
.hero-copy h1{font-size:16px;font-weight:700;margin-top:3px;letter-spacing:.06em}
.btn{position:absolute;left:381px;top:233px;width:87px;height:25px;background:var(--brand);color:var(--white);font-size:9px;font-weight:700;display:flex;align-items:center;justify-content:center;border-radius:2px}
.dots{position:absolute;top:293px;left:411px;display:flex;gap:4px}
.dots span{width:7px;height:7px;border:1px solid var(--white);border-radius:50%}
.dots span.on{border-color:#e14a52}
.intro{position:absolute;left:320px;top:364px;width:560px;text-align:center;font-size:11px;line-height:14.5px;color:var(--muted)}
.intro b{color:var(--ink)}
.stat{position:absolute;top:446px;height:69px;background:var(--tile);border:1px solid #eee;display:flex;align-items:center}
.stat .ico{width:61px;height:69px;background:var(--brand);display:flex;align-items:center;justify-content:center}
.stat .txt{padding-left:13px;color:var(--brand);font-size:10.5px;letter-spacing:.08em;line-height:14px}
.stat .num{display:block;color:#555;font-size:16px;font-weight:700;margin-top:4px}
.divider{position:absolute;left:244px;top:578px;width:692px;height:1px;background:var(--line)}
.check{position:absolute;left:586px;top:571px;width:18px;height:18px;border-radius:50%;background:var(--brand);display:flex;align-items:center;justify-content:center}
.section-title{position:absolute;top:602px;width:1200px;text-align:center;font-size:13px;font-weight:400;letter-spacing:.12em;color:#444}
.section-title b{color:#222;font-weight:700}
.card{position:absolute;top:676px;width:211px;height:201px;border:1px solid #eee;background:var(--white);text-align:center}
.card .photo{height:80px}
.card .badge{position:absolute;left:77px;top:-24px;width:56px;height:56px;border-radius:50%;background:var(--brand);border:3px solid var(--white);display:flex;align-items:center;justify-content:center}
.card h3{font-size:12.5px;font-weight:500;margin-top:15px;letter-spacing:.08em;color:#333}
.card p{font-size:8.4px;line-height:12.8px;color:var(--muted);padding:5px 10px 0;letter-spacing:.03em}
.practice-photo{position:absolute;left:172px;top:924px;width:417px;height:276px;
  background:linear-gradient(200deg,#f4f1e8 0%,#e9c26a 30%,#c9d6e4 55%,#3c5b86 80%,#243d63 100%)}
.practice{position:absolute;left:589px;top:924px;width:420px;height:276px;background:var(--brand);color:var(--white);padding:22px 25px 0;overflow:hidden}
.practice h2{font-size:21.5px;font-weight:700;letter-spacing:.06em}
.practice h4{font-size:11px;font-weight:500;letter-spacing:.1em;margin-top:4px}
.practice p{font-size:10px;line-height:14.2px;margin-top:14px;letter-spacing:.05em}
.practice .more{display:block;margin-top:2px;font-size:10.5px;line-height:13px}
</style>
</head>
<body>
<header class="hero" role="img" aria-label="Upward view of a glass office tower against a cloudy sky">
  <nav class="nav">
    <div class="brand"><span class="brand-mark"></span>Tembo &amp; Lusani</div>
    <div class="menu">
      <a class="active">Home</a><a>About Us</a><a>Our Professionals</a><a>Clients</a><a>Contact Us</a>
    </div>
  </nav>
  <div class="hero-copy">
    <p>To provide legal services focused on</p>
    <h1>Commercial Litigation, Construction Law &amp; Arbitration.</h1>
  </div>
  <div class="btn">KNOW MORE</div>
  <div class="dots"><span></span><span class="on"></span><span></span></div>
</header>

<p class="intro"><b>Tembo &amp; Lusani Advocates</b> are a specialist commercial law firm in Uganda focusing on commercial litigation, construction law and arbitration. We have excelled in our niche areas for over two decades and we continue to grow and be the firm choice in those practice areas.</p>

<div class="stat" style="left:243px;width:150px">
  <div class="ico"><svg width="34" height="28" viewBox="0 0 34 28" fill="#fff"><circle cx="11" cy="8" r="5"/><circle cx="23" cy="8" r="5"/><path d="M2 26c0-7 4-11 9-11s9 4 9 11zM14 26c0-7 4-11 9-11s9 4 9 11z"/></svg></div>
  <div class="txt">PARTNERS<span class="num">5</span></div>
</div>
<div class="stat" style="left:411px;width:150px">
  <div class="ico"><svg width="36" height="32" viewBox="0 0 36 32" fill="#fff"><circle cx="18" cy="7" r="5"/><circle cx="8" cy="12" r="4"/><circle cx="28" cy="12" r="4"/><circle cx="18" cy="19" r="4.5"/><path d="M1 24c0-4 3-7 7-7s7 3 7 7zM21 24c0-4 3-7 7-7s7 3 7 7zM10 31c0-5 4-8 8-8s8 3 8 8z"/></svg></div>
  <div class="txt">PEOPLE<span class="num">20+</span></div>
</div>
<div class="stat" style="left:579px;width:191px">
  <div class="ico"><svg width="32" height="32" viewBox="0 0 32 32" fill="none" stroke="#fff" stroke-width="2"><rect x="3" y="5" width="26" height="24" rx="2"/><line x1="3" y1="11" x2="29" y2="11"/><line x1="9" y1="2" x2="9" y2="8"/><line x1="23" y1="2" x2="23" y2="8"/><text x="16" y="25" fill="#fff" stroke="none" font-size="11" font-family="Roboto,sans-serif" font-weight="700" text-anchor="middle">55</text></svg></div>
  <div class="txt">YEAR OF COMBINED<br>EXPERIENCE<span class="num">55</span></div>
</div>
<div class="stat" style="left:785px;width:151px">
  <div class="ico"><svg width="38" height="32" viewBox="0 0 38 32" fill="#fff"><rect x="5" y="20" width="5" height="11"/><rect x="13" y="16" width="5" height="15"/><rect x="21" y="18" width="5" height="13"/><rect x="29" y="12" width="5" height="19"/><path d="M2 20l10-9 7 5 12-11" stroke="#fff" stroke-width="3" fill="none"/><path d="M27 3h8v8z"/></svg></div>
  <div class="txt">CASES<br>SOLVED<span class="num">350+</span></div>
</div>

<div class="divider"></div>
<div class="check"><svg width="10" height="10" viewBox="0 0 10 10"><path d="M2 5l2 2 4-4" stroke="#fff" stroke-width="1.6" fill="none"/></svg></div>
<h2 class="section-title">HOW <b>WE DO IT</b></h2>

<div class="card" style="left:244px">
  <div class="photo" role="img" aria-label="Judge's gavel beside law books" style="background:linear-gradient(90deg,#5a3a22,#2b1a10 50%,#8a5a3a)"></div>
  <div class="badge"><svg width="26" height="24" viewBox="0 0 26 24" fill="none" stroke="#fff" stroke-width="1.6"><line x1="13" y1="2" x2="13" y2="21"/><line x1="4" y1="5" x2="22" y2="5"/><line x1="8" y1="21" x2="18" y2="21"/><path d="M4 5l-3 8h6zM22 5l-3 8h6z"/><path d="M1 13a3 2 0 0 0 6 0M19 13a3 2 0 0 0 6 0"/></svg></div>
  <h3>Integrity</h3>
  <p>We maintain ethical behaviour and strict moral values. We are honest and trustworthy in our dealings with each other, with our clients and with all others with whom we deal.</p>
</div>
<div class="card" style="left:485px">
  <div class="photo" role="img" aria-label="Two business people shaking hands over a desk" style="background:linear-gradient(90deg,#e8ecef,#c9c2b6 45%,#3a3f48 75%,#1d2230)"></div>
  <div class="badge"><svg width="28" height="20" viewBox="0 0 28 20" fill="#fff"><path d="M1 5l6-3 5 2 4-2 6 1 5 4-4 5-5 5-4-2-3 1-4-4-6-2z"/></svg></div>
  <h3>Partnership</h3>
  <p>We partner with our clients and keep a close and interactive relationship that enriches our business knowledge and allows us to provide strategic, innovative and forward-thinking solutions fit to meet the challenges they face every day.</p>
</div>
<div class="card" style="left:722px">
  <div class="photo" role="img" aria-label="Hand drawing a rising efficiency curve on a dark teal board" style="background:linear-gradient(90deg,#123a4a,#1e5366 60%,#d9c4b0)"></div>
  <div class="badge"><svg width="24" height="26" viewBox="0 0 24 26" fill="none" stroke="#fff" stroke-width="2"><circle cx="12" cy="15" r="9"/><line x1="9" y1="3" x2="15" y2="3"/><line x1="12" y1="3" x2="12" y2="6"/><path d="M12 15V9"/><path d="M12 15l4 3"/></svg></div>
  <h3>Efficiency</h3>
  <p>We work to surpass our clients' expectations. We are practical and solution-driven in our approach. We are innovative and creative, and we focus sharply and firmly on the issues we undertake.</p>
</div>

<div class="practice-photo" role="img" aria-label="Upward view of sunlit glass skyscrapers"></div>
<section class="practice">
  <h2>PRACTICE AREAS</h2>
  <h4>CONSTRUCTION LAW</h4>
  <p>Our Construction Law department is headed by our Senior Partner Samuel Tembo, who is highly qualified and experienced in Construction law and in providing advice on contract management under the ARCON, BQS, TCF and CWS forms of contracts. We advise on all aspects of claim procedures as well as claim preparation and enforcement (or defence) strategies; advice on assessment and formulation of delay and disruption claims. We advise on local and international infrastructure disputes, arbitration and mediation. We advise clients on all their construction-related legal needs, from the drafting of the tender, procurement and project documentation to the resolution of disputes arising out of construction projects. With a client base that spans governments, energy and utility companies, lenders, developers, international and</p>
  <span class="more">Read More...</span>
</section>
</body>
</html>
```